Visual Print Advert for Hair & Makeup Artist

One page colour visual advertisement required for a hair and makeup artist business using pictures and logo with brief description and contact details. MUST have plain white background. All information will be provided I just need someone to put it in a good layout.
Professional, clean and appealing to the eye. Don't want it to look over crowded or busy.
Layout should feature 2-7 photos, without making the page look too busy. Can use any of the photos provided and you are welcome to crop them to change the orientation of the photo.
Content and typeface should fit in with logo and be modern but appeal to the female target audience of brides in Australia aged 22-40yo.
Advertisement is be be used in a bridal magazine and other print media for business advertising purposes.
Updates

Target Market(s)

Future brides in Australia aged 22 - 40yo - females only

Industry/Entity Type

Business

Colors
e34197
ffffff
eda3c7

Requirements
Must have
• White background
Should not have
• NO script writing as it doesn't fit with the logo.

```html
<!DOCTYPE html>
<html lang="en">
<head>
<meta charset="utf-8">
<title>Petalwood Makeup Artistry – Print Advert</title>
<link href="https://fonts.googleapis.com/css2?family=Lato:ital,wght@0,400;0,700;1,700&display=swap" rel="stylesheet">
<style>
  :root {
    --pink: #e34197;
    --pink-soft: #eda3c7;
    --white: #ffffff;
    --grey-text: #5a5a5a;
    --ink: #3a3a3a;
    --frame: #ffffff;
  }
  * { box-sizing: border-box; margin: 0; padding: 0; }
  html, body { width: 849px; height: 1200px; overflow: hidden; background: var(--white); }
  .advert {
    position: relative;
    width: 849px;
    height: 1200px;
    background: var(--white);
    font-family: "Lato", sans-serif;
    overflow: hidden;
  }
  .accent-band { position: absolute; background: var(--pink); }
  .accent-band--top { left: -20px; top: -10px; width: 360px; height: 90px; transform: rotate(-3deg); }
  .accent-band--mid { left: -30px; top: 560px; width: 910px; height: 150px; transform: rotate(-2deg); }
  .accent-band--soft { left: 260px; top: 520px; width: 600px; height: 40px; background: var(--pink-soft); transform: rotate(-2deg); }

  .photo {
    position: absolute;
    border: 8px solid var(--frame);
    box-shadow: 0 3px 10px rgba(0,0,0,0.25);
  }
  .photo--hero {
    left: 320px; top: 0; width: 529px; height: 520px;
    border: none; box-shadow: none;
    background: radial-gradient(ellipse at 50% 45%, #e8c9b6 0%, #c49a84 40%, #5b4438 80%, #e9e3df 100%);
  }
  .photo--portrait-bw {
    left: 40px; top: 40px; width: 260px; height: 190px; transform: rotate(-8deg);
    background: linear-gradient(135deg, #d8d8d8, #7a7a7a);
  }
  .photo--veil {
    left: 22px; top: 250px; width: 230px; height: 190px; transform: rotate(6deg);
    background: linear-gradient(160deg, #f2ece8, #b99583);
  }
  .photo--bride-smile {
    left: 36px; top: 460px; width: 260px; height: 220px; transform: rotate(-5deg);
    background: linear-gradient(150deg, #d7b29c, #6e5144);
  }
  .photo--bridal-party {
    left: 305px; top: 545px; width: 255px; height: 195px; transform: rotate(-1deg);
    background: linear-gradient(180deg, #cfc6c0, #e9e4e1 60%, #a88f82);
  }
  .photo--profile {
    left: 565px; top: 525px; width: 250px; height: 215px; transform: rotate(6deg);
    background: linear-gradient(140deg, #e3cbbb, #8a6252);
  }

  .brand {
    position: absolute; left: 0; top: 784px; width: 849px;
    display: flex; align-items: center; justify-content: center; gap: 14px;
  }
  .brand__dot {
    width: 18px; height: 18px; border-radius: 50%; background: var(--pink);
  }
  .brand__name {
    font-weight: 700; font-size: 44px; line-height: 1;
    color: var(--ink);
  }

  .credentials {
    position: absolute; left: 85px; top: 878px; width: 680px; height: 64px;
    border: 2px solid var(--pink); border-radius: 14px;
    display: flex; align-items: center; justify-content: center; text-align: center;
    font-style: italic; font-weight: 700; font-size: 19px; line-height: 1.3;
    color: #333;
  }
  .intro {
    position: absolute; left: 60px; top: 962px; width: 729px; text-align: center;
    font-size: 18px; line-height: 1.4; color: var(--grey-text);
  }
  .call {
    position: absolute; left: 215px; top: 1036px; width: 420px; height: 54px;
    border: 2px solid var(--pink); border-radius: 27px;
    display: flex; align-items: center; justify-content: center;
    font-weight: 700; font-size: 30px; color: var(--pink); letter-spacing: 1px;
  }
  .contact-band {
    position: absolute; left: 0; top: 1112px; width: 849px; height: 88px;
    background: var(--pink); color: var(--white); text-align: center;
    display: flex; flex-direction: column; justify-content: center; gap: 6px;
  }
  .contact-band__email { font-size: 19px; }
  .contact-band__web { font-size: 19px; letter-spacing: 3px; }
</style>
</head>
<body>
<main class="advert">
  <div class="accent-band accent-band--top"></div>
  <div class="accent-band accent-band--soft"></div>
  <div class="accent-band accent-band--mid"></div>

  <div class="photo photo--hero" role="img" aria-label="Close-up portrait of a bride with finished makeup and veil"></div>
  <div class="photo photo--portrait-bw" role="img" aria-label="Black and white bridal portrait"></div>
  <div class="photo photo--veil" role="img" aria-label="Bride wearing a veil, side view"></div>
  <div class="photo photo--bride-smile" role="img" aria-label="Smiling bride with styled hair"></div>
  <div class="photo photo--bridal-party" role="img" aria-label="Bride with her bridesmaids"></div>
  <div class="photo photo--profile" role="img" aria-label="Bride in profile with updo hairstyle"></div>

  <header class="brand">
    <span class="brand__dot"></span>
    <span class="brand__name">Petalwood Makeup Artistry</span>
  </header>

  <p class="credentials">Professionally trained and certified mobile Hair &amp; Makeup Artists with<br>over 10 years experience</p>

  <p class="intro">We specialise in naturally enhancing your beauty to have you looking and feeling your<br>best on your special day.</p>

  <div class="call">CALL US: : 0400 123 456</div>

  <footer class="contact-band">
    <div class="contact-band__email">Email: mia@petalwoodmakeup.com.au</div>
    <div class="contact-band__web">www.petalwoodmakeup.com.au</div>
  </footer>
</main>
</body>
</html>
```